Webdesign für lokalen Dart-Shop
Zielgruppe
Wir sind ein lokaler Dart-Shop in Hamburg, welcher in Norddeutschland sehr beliebt ist und bundesweit das Größte Angebot bietet. Durch unseren Online-Shop möchte wir unseren Radius erweitern.
Zielgruppe: Dart Anfänger, Fortgeschrittene sowie Vereine und Unternehmen
Aufgabenstellung
In jedem Fall das Haupt-Element unseres Logo´s, einer Dart-Scheibe.

```html
<!DOCTYPE html>
<html lang="de">
<head>
<meta charset="utf-8">
<title>Pfeilwerk Nord – Dartshop</title>
<link href="https://fonts.googleapis.com/css2?family=Roboto:wght@400;500;700&family=Open+Sans:wght@400;600;700&display=swap" rel="stylesheet">
<style>
  :root {
    --header-bg: #2e2e2e;
    --footer-bg: #000000;
    --side-bg: #f2f2f2;
    --page-bg: #ffffff;
    --red: #b81c1c;
    --red-light: #c84a48;
    --nav-active: #c0272d;
    --heading: #3a3a3a;
    --body-text: #333333;
    --light-text: #ffffff;
    --photo-dark: #3b3b3b;
  }
  * { margin: 0; padding: 0; box-sizing: border-box; }
  html, body { width: 1200px; height: 800px; overflow: hidden; }
  body {
    background: var(--side-bg);
    font-family: "Open Sans", Arial, sans-serif;
    position: relative;
  }
  .site-header {
    position: absolute; left: 0; top: 0;
    width: 1200px; height: 80px;
    background: var(--header-bg);
  }
  .brand {
    position: absolute; left: 340px; top: 18px;
    display: flex; align-items: center; gap: 8px;
  }
  .brand-mark {
    width: 44px; height: 44px; border-radius: 50%;
    background: #e9e9e9;
  }
  .brand-name {
    font-family: "Roboto", Arial, sans-serif;
    font-weight: 500; font-size: 13px;
    color: var(--light-text);
  }
  .main-nav {
    position: absolute; left: 512px; top: 60px;
    display: flex; gap: 4px;
  }
  .main-nav a {
    display: block; width: 46px; height: 14px;
    font-size: 7px; line-height: 14px; text-align: center;
    color: var(--light-text); text-decoration: none;
  }
  .main-nav a.is-active { background: var(--nav-active); }
  .page-column {
    position: absolute; left: 328px; top: 80px;
    width: 536px; height: 490px;
    background: var(--page-bg);
  }
  .hero {
    position: relative; width: 536px; height: 230px;
    background: linear-gradient(110deg, var(--photo-dark) 0%, #4a4a4a 35%, #9a9a9a 55%, #5a5a5a 75%, #2a2a2a 100%);
  }
  .hero-band { position: absolute; left: 0; top: 0; }
  .intro { padding: 30px 14px 0; }
  .intro h1 {
    font-family: "Roboto", Arial, sans-serif;
    font-weight: 500; font-size: 22px;
    color: var(--heading);
  }
  .intro p {
    margin-top: 12px; width: 400px;
    font-size: 7px; line-height: 11px;
    color: var(--body-text);
  }
  .gallery {
    display: flex; gap: 18px;
    padding: 20px 10px 0;
  }
  .gallery-tile { width: 160px; height: 98px; }
  .tile-storefront { background: linear-gradient(90deg, #d8d8d8 0%, #a24a36 50%, #3f4a5c 100%); }
  .tile-boards { background: linear-gradient(180deg, #4a3a3a 0%, #2a2a2a 55%, #c7c0bb 100%); }
  .tile-cafe { background: linear-gradient(135deg, #5a4a46 0%, #e8e4e0 55%, #7a2a2a 100%); }
  .site-footer {
    position: absolute; left: 0; top: 570px;
    width: 1200px; height: 230px;
    background: var(--footer-bg);
    color: var(--light-text);
    font-size: 6.5px; line-height: 11.5px;
    font-weight: 600;
  }
  .footer-col { position: absolute; top: 12px; }
  .footer-col h2 { font-size: 6.5px; font-weight: 700; }
  .footer-col ul { list-style: none; }
  .col-more { left: 355px; width: 152px; white-space: nowrap; }
  .col-contact { left: 514px; width: 170px; white-space: nowrap; }
  .col-route { left: 695px; width: 165px; }
  .col-contact h2 + ul + h2 { margin-top: 11.5px; }
  .address { color: var(--red); }
</style>
</head>
<body>
  <header class="site-header">
    <div class="brand">
      <span class="brand-mark"></span>
      <span class="brand-name">Pfeilwerk Nord</span>
    </div>
    <nav class="main-nav">
      <a class="is-active" href="#">Home</a>
      <a href="#">Shop</a>
      <a href="#">News</a>
    </nav>
  </header>

  <main class="page-column">
    <section class="hero" role="img" aria-label="Schwarz-weißes Foto: Hand hält einen Dartpfeil kurz vor dem Wurf">
      <svg class="hero-band" width="536" height="230" viewBox="0 0 536 230" aria-hidden="true">
        <polygon points="0,176 315,230 0,230" fill="var(--red-light)"/>
        <polygon points="315,230 536,172 536,230" fill="var(--red)"/>
      </svg>
    </section>
    <section class="intro">
      <h1>Willkommen in unserem Dartshop</h1>
      <p>Wir führen eine Vielzahl an Produkten, sollte aber dennoch ein Artikel nicht dabei sein einfach eine kurze E-Mail an: info@pfeilwerk-nord.de schicken. Wir setzen uns mit Ihnen umgehend in Verbindung.</p>
    </section>
    <section class="gallery">
      <div class="gallery-tile tile-storefront" role="img" aria-label="Foto: Eingang und Schaufenster des Ladens"></div>
      <div class="gallery-tile tile-boards" role="img" aria-label="Foto: Dartscheiben und Zubehör an der Ladenwand"></div>
      <div class="gallery-tile tile-cafe" role="img" aria-label="Foto: Kaffee-Ecke mit Auslage im Laden"></div>
    </section>
  </main>

  <footer class="site-footer">
    <div class="footer-col col-more">
      <h2>MEHR ÜBER</h2>
      <ul>
        <li>Impressum</li>
        <li>Kontakt</li>
        <li>Versand- &amp; Zahlungsbedingungen</li>
        <li>Widerrufsrecht &amp; Muster-Widerrufsformular</li>
        <li>AGB</li>
        <li>Privatsphäre und Datenschutz</li>
        <li>Callback Service</li>
      </ul>
    </div>
    <div class="footer-col col-contact">
      <h2>KONTAKT</h2>
      <ul>
        <li>Tel: 040 555 218 40 - 0</li>
        <li>Fax: 040 555 218 40 - 9</li>
        <li>kontakt@pfeilwerk-nord.de</li>
        <li>www.pfeilwerk-nord.de</li>
      </ul>
      <h2>SHOP ÖFFNUNGSZEITEN</h2>
      <ul>
        <li>Montag - Samstag 12:00 - 18:00</li>
      </ul>
    </div>
    <div class="footer-col col-route">
      <h2>ANFAHRT</h2>
      <ul>
        <li class="address">Pfeilwerk Nord GmbH</li>
        <li class="address">Lindenweg Nr. 12</li>
        <li class="address">20099 Hamburg</li>
        <li>Parkmöglichkeiten direkt vor dem Ladengeschäft oder in der Einbahnstraße, welche direkt um das Grundstück herum führt. S-Bahn Lindenweg nur 200m entfernt!</li>
      </ul>
    </div>
  </footer>
</body>
</html>
```